Community Bank Web Design

Design a homepage and internal product page for a community bank. Needs to be mobile friendly, minimal scrolling on home. Create the homepage look & feel, then use the same aesthetic to create the product page for the personal checking account page.

Wireframes, logo variations, and color scheme attached.

New brand identity:
• Open, Fresh, Younger, Bright, Bold, New, Innovative.
• Inviting, approachable, friendly, trustworthy.
• Imagine a young family purchasing their first home as the target audience.
You do not have to stick to the exact layout of the wireframes, as long as all of the elements are present.

All navigation elements are specified in wireframes. There are three versions of the homepage – Personal Home, Business Home, Wealth Management Home – you may design whichever version you prefer.

For internal page – please design the Checking product page, included in wireframes.

NOTE: Submit your homepage design first. I will provide feedback on your design direction, then you can use that to move forward with the internal page design.

Design direction--
Some banking / financial sites we like for their fresh/bold/open look:
velmorant.com
quastel.ca
rpwfinancial.org
kdh.co.nz
yarbel.com
pettigrubank.com
uvm.co.nz

Target Market(s)

The target market for the personal homepage varies. Adults in the midwest, 25 - 60, who are striving to build their savings and manage their money. Often buying homes or refinancing their homes to make renovations, or planning for retirement.

For the business homepage, the target market are small to mid-market business owners striving to grow their business and manage their company.

Industry/Entity Type

Financial

Requirements
Must have
• colors: CRIMSON #a20c33,
FOREST GREEN #004f38
GOLD #e6a513

File format for design submission must be layered PSD (Please organize layers into recognizable folders like "menu" and "footer")

To make the design "mobile friendly" please create a grid-based layout. http://www.dorvané.com/patterns/showPattern.php?patternID=grid-based-layout
http://www.brindlequarterly.com/2007/04/14/designing-with-grid-based-approach/

```html
<!DOCTYPE html>
<html lang="en">
<head>
<meta charset="utf-8">
<title>Harrow Creek Bank — Personal</title>
<link href="https://fonts.googleapis.com/css2?family=Roboto:wght@300;400;500;700;900&family=Raleway:wght@400;500&display=swap" rel="stylesheet">
<style>
:root{
  --crimson:#a20c33;
  --forest:#004f38;
  --forest-deep:#00382a;
  --sage:#5a8a7a;
  --sea:#5a9a85;
  --gold:#e6a513;
  --gold-bright:#f5a800;
  --ink:#333;
  --muted:#777;
  --panel:#f6f6f6;
}
*{margin:0;padding:0;box-sizing:border-box}
html,body{width:1071px;height:1200px;overflow:hidden;background:#fff}
body{position:relative;font-family:'Roboto',sans-serif;color:var(--ink)}
.abs{position:absolute}
a{color:inherit}

/* utility bar */
.utility-bar{left:0;top:0;width:1071px;height:41px;background:var(--crimson);color:#fff;font-size:11px;font-weight:500;letter-spacing:.3px}
.segment-nav{left:126px;top:13px;display:flex}
.segment-nav span{padding:0 11px;border-left:1px solid rgba(255,255,255,.6);line-height:12px}
.segment-nav span:first-child{border:0;padding-left:0}
.segment-nav span:last-child{border:0;padding-left:0}
.caret{left:145px;top:35px;width:0;height:0;border:6px solid transparent;border-bottom-color:#fff;border-top:0}
.utility-links{left:503px;top:15px;display:flex;gap:24px;font-weight:400;font-size:11.5px}
.utility-links span{display:flex;align-items:center;gap:6px}
.site-search{left:789px;top:10px;width:152px;height:21px;border-bottom:1px solid #fff;font-size:11px;font-weight:400;padding-top:3px}
.site-search svg{position:absolute;right:4px;top:4px}

/* header */
.brand{left:122px;top:70px;display:flex;align-items:center;gap:10px}
.brand-mark{width:48px;height:48px;border-radius:50%;background:var(--crimson)}
.brand-name{font-size:31px;font-weight:400;color:var(--crimson);letter-spacing:-.3px}
.brand-note{left:124px;top:122px;font-size:6px;color:#222}
.main-nav{top:70px;height:62px;display:flex;flex-direction:column;align-items:center;font-size:11.5px;font-weight:500;letter-spacing:.4px;color:#444}
.main-nav svg{margin-bottom:8px}
.main-nav.active{color:var(--forest)}
.nav-divider{top:70px;width:1px;height:62px;background:#e5e5e5}

/* hero */
.hero{left:0;top:160px;width:1071px;height:321px;background:linear-gradient(100deg,#c9a24a 0%,#7b6b45 25%,#6c6a55 45%,#55543f 70%,#4e5a38 100%)}
.login-panel{left:116px;top:160px;width:317px;height:321px;background:rgba(255,255,255,.28)}
.login-title{left:147px;top:182px;font-size:20px;font-weight:700;color:#fff}
.login-rule{left:147px;top:218px;width:250px;height:1px;background:rgba(255,255,255,.8)}
.field{left:148px;width:254px;height:42px;background:#fff;border-radius:3px;font-size:11px;font-style:italic;color:#999;display:flex;align-items:center;padding-left:14px;gap:9px}
.forgot{left:205px;top:361px;font-size:9.5px;font-style:italic;text-decoration:underline;color:#fff}
.login-btn{left:301px;top:349px;width:99px;height:32px;background:var(--crimson);border-radius:3px;color:#fff;font-size:13px;display:flex;align-items:center}
.login-btn span{width:66px;text-align:center}
.login-btn i{width:33px;height:32px;background:#c8103f;border-radius:0 3px 3px 0;display:flex;align-items:center;justify-content:center}
.enroll{left:189px;top:416px;font-size:9.5px;color:#fff}
.enroll b{color:var(--gold);font-weight:400;margin-left:18px}
.loan-bar{left:116px;top:441px;width:317px;height:40px;background:var(--crimson);color:#fff;font-size:18px;display:flex;align-items:center;padding-left:52px;gap:10px}
.loan-bar i{width:28px;height:28px;border-radius:50%;background:#b51a42;display:flex;align-items:center;justify-content:center}
.hero-headline{left:485px;top:180px;font-size:52px;font-weight:900;color:#fff;line-height:55px;letter-spacing:2px}
.hero-tag{left:484px;top:298px;font-size:37px;font-weight:300;color:var(--gold-bright);letter-spacing:-.8px}
.hero-sub{left:484px;top:340px;font-size:28px;font-weight:300;color:#fff;letter-spacing:-.6px}
.btn{background:var(--gold-bright);color:#fff;display:flex;align-items:center;justify-content:center;letter-spacing:.3px}
.hero-btn{left:485px;top:395px;width:99px;height:35px;font-size:13px;box-shadow:0 3px 0 #c98a00}
.hero-arrow{top:305px}
.hero-dots{left:620px;top:450px;display:flex;gap:8px}
.hero-dots i{width:36px;height:2px;background:rgba(255,255,255,.35)}
.hero-dots i.on{background:#fff}
.hero-dots i.gold{background:var(--gold)}

/* feature tiles */
.tile{top:529px;width:278px;height:264px;color:#fff;text-align:center;padding-top:26px}
.tile h3{font-family:'Raleway',sans-serif;font-weight:500;font-size:16.5px;letter-spacing:.6px;margin:18px 0 12px}
.tile p{font-size:10.6px;line-height:12.2px;padding:0 30px}
.tile .btn{margin:22px auto 0;height:28px;font-size:10.5px;display:inline-flex;padding:0 10px}
.tile-mobile{left:116px;background:var(--forest-deep)}
.tile-home{left:395px;background:var(--sage)}
.tile-card{left:673px;background:var(--sea)}

/* home equity */
.equity-art{left:103px;top:845px;width:242px;height:165px;background:radial-gradient(ellipse at 50% 55%,#c9b45a 0%,#9aa07a 35%,#d8d8d0 65%,#fff 85%)}
.equity-title{left:360px;top:835px;font-family:'Raleway',sans-serif;font-size:19px;font-weight:500;color:#333}
.equity-copy{left:361px;top:868px;width:245px;font-size:10.1px;line-height:14.3px;letter-spacing:-.1px;color:var(--muted);text-align:justify}
.equity-btn{left:360px;top:1011px;width:99px;height:35px;font-size:13px;box-shadow:0 3px 0 #c98a00}

/* rates */
.rates{left:654px;top:830px;width:297px;height:217px;background:var(--panel)}
.rate-tabs{left:654px;top:830px;width:297px;height:36px;background:#e9e9e9;display:flex;font-size:9px}
.rate-tabs span{width:81px;display:flex;align-items:center;justify-content:center}
.rate-tabs .on{background:var(--panel);color:var(--crimson);border-top:2px solid var(--crimson)}
.rate-note{left:666px;top:879px;font-size:8.5px;color:#333}
.rate-row{left:654px;width:297px;height:42px;display:flex;align-items:center;padding-left:14px;font-size:12.5px}
.rate-row b{font-weight:400;font-size:26px;color:var(--gold-bright);margin-left:19px}
.rate-row.dark{top:898px;background:var(--forest-deep);color:#fff}
.rate-row.light{top:938px;color:#333}
.rate-fine{left:668px;top:999px;font-size:8.5px;color:#333;line-height:14px}
.rate-fine .call{color:var(--crimson);font-size:14px}
.rate-fine .strong{font-size:12px;color:#222}

/* footer */
.footer{left:0;top:1091px;width:1071px;height:109px;background:var(--crimson);color:#fff;text-align:center;font-size:9px}
.footer-links{display:flex;justify-content:center;gap:14px}
.footer-links a{text-decoration:underline}
</style>
</head>
<body>

<header>
  <div class="abs utility-bar">
    <nav class="abs segment-nav"><span>PERSONAL</span><span>BUSINESS</span><span>WEALTH</span><span>MANAGEMENT</span></nav>
    <div class="abs utility-links">
      <span><svg width="11" height="11" viewBox="0 0 12 12"><circle cx="5" cy="5" r="3.6" fill="none" stroke="#fff" stroke-width="1.8"/><path d="M7.6 7.6 11 11" stroke="#fff" stroke-width="2"/></svg>FIND A BRANCH OR ATM</span>
      <span><svg width="8" height="12" viewBox="0 0 8 12"><rect x="1" y="1" width="6" height="10" rx="1" fill="none" stroke="#fff" stroke-width="1.4"/></svg>CONTACT US</span>
    </div>
    <div class="abs site-search">Search
      <svg width="10" height="10" viewBox="0 0 12 12"><circle cx="5" cy="5" r="3.6" fill="none" stroke="#fff" stroke-width="1.8"/><path d="M7.6 7.6 11 11" stroke="#fff" stroke-width="2"/></svg>
    </div>
  </div>
  <div class="abs caret"></div>

  <div class="abs brand"><div class="brand-mark"></div><div class="brand-name">Harrow Creek Bank</div></div>
  <div class="abs brand-note">Member FDIC</div>

  <div class="abs main-nav active" style="left:544px">
    <svg width="20" height="20" viewBox="0 0 20 20"><rect x="1" y="1" width="8" height="8" rx="1" fill="var(--forest)"/><rect x="11" y="1" width="8" height="8" rx="1" fill="var(--forest)"/><rect x="1" y="11" width="8" height="8" rx="1" fill="var(--forest)"/><rect x="11" y="11" width="8" height="8" rx="1" fill="var(--forest)"/></svg>
    PRODUCT AND SERVICES</div>
  <div class="abs nav-divider" style="left:708px"></div>
  <div class="abs main-nav" style="left:734px">
    <svg width="14" height="20" viewBox="0 0 14 20"><path d="M2 6a5 5 0 1 1 7 4.5c-1.5.7-2 1.5-2 3" fill="none" stroke="#444" stroke-width="3"/><rect x="5.5" y="16" width="3" height="3" fill="#444"/></svg>
    WHY HCB?</div>
  <div class="abs nav-divider" style="left:822px"></div>
  <div class="abs main-nav" style="left:841px">
    <svg width="22" height="20" viewBox="0 0 22 20"><circle cx="5" cy="6" r="3" fill="#444"/><circle cx="17" cy="6" r="3" fill="#444"/><circle cx="11" cy="5" r="3.6" fill="#444"/><path d="M0 17c0-5 3-7 5-7s5 2 5 7Z M12 17c0-5 3-7 5-7s5 2 5 7Z M5 19c0-6 3-9 6-9s6 3 6 9Z" fill="#444"/></svg>
    CUSTOMER CENTER</div>
</header>

<section>
  <div class="abs hero" role="img" aria-label="Photo of a two-storey family house with a stone chimney among trees"></div>
  <div class="abs login-panel"></div>
  <div class="abs login-title">Log on to E-banking</div>
  <div class="abs login-rule"></div>
  <div class="abs field" style="top:240px">
    <svg width="12" height="12" viewBox="0 0 12 12"><circle cx="4.5" cy="4.5" r="3.3" fill="none" stroke="#bbb" stroke-width="2"/><path d="M7 7 11 11" stroke="#bbb" stroke-width="2.2"/></svg>
    Account type
    <svg style="position:absolute;right:12px" width="12" height="8" viewBox="0 0 12 8"><path d="M1 1 6 6 11 1" fill="none" stroke="#aaa" stroke-width="1.4"/></svg>
  </div>
  <div class="abs field" style="top:295px">
    <svg width="12" height="12" viewBox="0 0 12 12"><circle cx="6" cy="4" r="3" fill="#ddd"/><path d="M0 12c0-4 3-5 6-5s6 1 6 5Z" fill="#ddd"/></svg>
    User id
  </div>
  <div class="abs forgot">Forgot your user id?</div>
  <div class="abs login-btn"><span>Log in</span><i><svg width="9" height="12" viewBox="0 0 9 12"><path d="M2 5V3.5a2.5 2.5 0 0 1 5 0V5" fill="none" stroke="#fff" stroke-width="1.4"/><rect x="1" y="5" width="7" height="6" fill="none" stroke="#fff" stroke-width="1.4"/></svg></i></div>
  <div class="abs enroll">New to HCB online? <b>ENROLL</b><b style="margin-left:14px">LERN MORE</b></div>
  <div class="abs loan-bar"><i><svg width="13" height="13" viewBox="0 0 13 13"><path d="M2 11 3 8 9 2 11 4 5 10Z" fill="#fff"/></svg></i>APPLY FOR A LOAN</div>

  <h1 class="abs hero-headline">Dreaming of your<br>first home?</h1>
  <div class="abs hero-tag">Let's make it possible.</div>
  <div class="abs hero-sub">Talk to a mortgage banker today.</div>
  <div class="abs btn hero-btn">LERN MORE</div>
  <svg class="abs hero-arrow" style="left:66px" width="22" height="36" viewBox="0 0 22 36"><path d="M18 2 3 18 18 34" fill="none" stroke="#fff" stroke-width="2"/></svg>
  <svg class="abs hero-arrow" style="left:982px" width="22" height="36" viewBox="0 0 22 36"><path d="M4 2 19 18 4 34" fill="none" stroke="#fff" stroke-width="2"/></svg>
  <div class="abs hero-dots"><i></i><i class="on"></i><i class="gold"></i></div>
</section>

<section>
  <article class="abs tile tile-mobile">
    <svg width="24" height="42" viewBox="0 0 24 42"><rect x="2" y="2" width="20" height="38" rx="2" fill="none" stroke="#fff" stroke-width="2.5"/><path d="M2 8h20M2 34h20" stroke="#fff" stroke-width="2"/></svg>
    <h3>MOBILE DEPOSIT. IT'S EASY!</h3>
    <p>Vivamus sagittis lacuson augue laoreet rutrum faucibus dolor auctor. Cras mattis consectetur purus sit amet fermentum. Vivamus sagittis lacuson augue laoreet rutrum faucibus dolor auctor. Cras mattis consectetur purus sit amet</p>
    <div class="btn" style="width:82px">LERN MORE</div>
  </article>
  <article class="abs tile tile-home">
    <svg width="36" height="40" viewBox="0 0 36 40"><path d="M4 18 18 4 32 18V37H4Z" fill="none" stroke="#fff" stroke-width="3.5" stroke-linejoin="round"/></svg>
    <h3>LOOKING FOR NEW HOME</h3>
    <p>Vivamus sagittis lacuson augue laoreet rutrum faucibus dolor auctor. Cras mattis consectetur purus sit amet fermentum. Vivamus sagittis lacuson augue laoreet rutrum faucibus dolor auctor. Cras mattis consectetur purus sit amet</p>
    <div class="btn">FIND YOU MORTGAGE BANKER</div>
  </article>
  <article class="abs tile tile-card">
    <svg width="56" height="40" viewBox="0 0 56 40"><rect x="2" y="10" width="52" height="24" fill="none" stroke="#fff" stroke-width="2.5"/><text x="28" y="28" fill="#fff" font-size="14" text-anchor="middle" font-family="Roboto,sans-serif">$</text></svg>
    <h3>VELORA DEBIT CARD</h3>
    <p>Vivamus sagittis lacuson augue laoreet rutrum faucibus dolor auctor. Cras mattis consectetur purus sit amet fermentum. Vivamus sagittis lacuson augue laoreet rutrum faucibus dolor auctor. Cras mattis consectetur purus sit amet</p>
    <div class="btn" style="width:82px">LERN MORE</div>
  </article>
</section>

<section>
  <div class="abs equity-art" role="img" aria-label="Illustration of a small yellow house resting on banknotes and a calculator"></div>
  <h2 class="abs equity-title">Home Equity Lines of Credit</h2>
  <p class="abs equity-copy">Lorem ipsum dolor sit amet, consectetur adipiscing elit. Nulla quam velit, vulputate eu pharetra nec, mattis ac neque. Duis vulputate commodo lectus, ac blandit elit tincidunt id. Sed rhoncus, tortor sed eleifend tristique, tortor mauris molestie elit, et lacinia ipsum quam nec dui. Quisque nec mauris sit amet elit iaculis pretium sit amet quis magna. Aenean velit odio, elementum in tempus ut, vehicula eu diam. Pellentesque rhoncus aliquam mattis. Ut vulputate eros</p>
  <div class="abs btn equity-btn">LERN MORE</div>

  <div class="abs rates"></div>
  <div class="abs rate-tabs"><span class="on">LOANS</span><span>DEPOSITS</span></div>
  <div class="abs rate-note">(As low as)</div>
  <div class="abs rate-row dark">5 year fixed Mortgage <b>2.99%</b></div>
  <div class="abs rate-row light">Velora Credit Card <span style="margin-left:26px">:</span> <b>8.24%</b></div>
  <div class="abs rate-fine">RATES VARY DAILY AND DEPEND ON MANY FACTORS.<br><span class="call">CALL TODAY</span> TO FIND YOUR <span class="strong">BEST OPTIONS.</span></div>
</section>

<footer class="abs footer">
  <div class="footer-links" style="margin-top:34px"><a>About Harrow</a><a>Creek Bank</a><a>Careers</a><a>Privacy policy</a><a>investees relation links</a></div>
  <div class="footer-links" style="margin-top:8px"><a>Security</a><a>Members FDCI</a><span>CRA</span><a>Other required information</a></div>
  <div style="margin-top:14px;font-size:8.5px">Copyright © Harrowcreek2014</div>
</footer>

</body>
</html>
```